Chocolate company needing sticker for products

I have a small chocolate company Willow Bend Sweets in Austin Texas. I make all vegan, gluten free, organic, faire trade chocolate that tastes amazing! It is allergy friendly approvable by all ages. I want to have a great sticker that i can put on our boxes and bags. I am using a lot of natural craft color and brown. I am open to color options possibly for different flavors. I want the packaging to reflect the basis of my company. It is all handmade by me but i don't want it to have to much of a crafty look to it. I have attached the logo designs I have. it the sticker can have som of the bullet points about the company that would be great. But it needs to say Locally Made in Austin Texas. it also has to have the company address.
418 West Cobbler Ridge Rd #207 Austin Tx 78745. These things are required by the state for food regulations. I want something that looks great and I can be really proud to put on my product! Thanks so much for all of your help in advance. Dot

I also need some other information added to the sticker. Website which is willowbendsweetsatx.com 

Phone number 512.368.4175. Instagram willowbendsweets. Thanks for your hard work! 

Industry/Entity Type

Chocolate Company

Requirements
Must have
• The logo is added at the bottom as well as designs I like I want to have a professional look but it to be approvable by all consumers. I will gig feed back as i see what designs come through. This will probably fold out into a multi design project so i will be looking for assistance on other areas of this as well. Thanks

```html
<!DOCTYPE html>
<html lang="en">
<head>
<meta charset="utf-8">
<title>Willow Bend Sweets – Product Stickers</title>
<link rel="stylesheet" href="https://fonts.googleapis.com/css2?family=Source+Sans+3:wght@400;600;700&family=Libre+Baskerville:ital,wght@1,400;1,700&display=swap">
<style>
  :root {
    --backdrop: #cdb291;
    --ink: #111111;
    --paper: #ffffff;
    --lavender: #c8b9e6;
    --blush: #f6c5c2;
    --peach: #f8c8ae;
    --lemon: #f6e84e;
    --apricot: #fbc08a;
  }
  * { box-sizing: border-box; margin: 0; padding: 0; }
  html, body { width: 1200px; height: 840px; overflow: hidden; }
  body {
    background: var(--backdrop);
    font-family: "Source Sans 3", Arial, sans-serif;
  }
  .sticker-row { position: relative; width: 1200px; height: 840px; }
  .sticker {
    position: absolute;
    top: 100px;
    width: 150px;
    height: 560px;
  }
  .sticker--noir-full { left: 100px; }
  .sticker--framed    { left: 380px; }
  .sticker--noir-inset{ left: 660px; }
  .sticker--white-inset{ left: 940px; }
  .sticker__shape { position: absolute; inset: 0; width: 150px; height: 560px; }
  .label {
    position: absolute;
    inset: 0;
    padding: 0 12px;
    color: var(--ink);
    text-align: left;
  }
  .label--light { color: var(--paper); }
  .ornament {
    display: block;
    width: 18px;
    height: 14px;
    margin: 0 auto;
    background: currentColor;
    border-radius: 50% 50% 20% 20%;
  }
  .ornament--top { margin-top: 118px; }
  .ornament--bottom { margin-top: 16px; border-radius: 20% 20% 50% 50%; }
  .tagline {
    margin-top: 20px;
    font-family: "Libre Baskerville", Georgia, serif;
    font-style: italic;
    font-size: 6.4px;
    line-height: 1.35;
    text-align: right;
  }
  .tagline strong { font-weight: 700; }
  .rule { border-top: 2px dotted currentColor; margin: 5px 0; }
  .origin {
    font-weight: 600;
    font-size: 17px;
    line-height: 1.05;
  }
  .address { font-size: 6.2px; margin-top: 2px; white-space: nowrap; }
  .brand-name {
    text-align: center;
    font-weight: 700;
    text-transform: uppercase;
    line-height: 0.95;
    padding: 4px 0 2px;
  }
  .brand-name__big { display: block; font-size: 31px; }
  .brand-name__small { display: block; font-size: 17px; margin: 3px 0; }
  .contact { font-size: 12px; line-height: 1.45; margin-top: 6px; }
  .contact__item { display: flex; align-items: center; gap: 4px; white-space: nowrap; }
  .contact__web { font-size: 11.2px; }
  .icon { width: 9px; height: 9px; flex: none; }
  .icon--square { display: inline-block; background: currentColor; border-radius: 2px; }
</style>
</head>
<body>
<main class="sticker-row">

  <!-- Black sticker, full bleed -->
  <article class="sticker sticker--noir-full">
    <svg class="sticker__shape" viewBox="0 0 150 560" aria-hidden="true">
      <defs>
        <linearGradient id="notch-glow" x1="0" y1="0" x2="1" y2="1">
          <stop offset="0" stop-color="#f6c5c2"/>
          <stop offset="0.6" stop-color="#fbc08a"/>
          <stop offset="1" stop-color="#f6e84e"/>
        </linearGradient>
      </defs>
      <polygon points="40,22 60,6 80,20 60,42" fill="url(#notch-glow)"/>
      <path d="M0,30 L40,20 L60,42 L80,18 L110,40 L150,8 L150,548 L0,560 Z" fill="#111111"/>
    </svg>
    <div class="label label--light">
      <span class="ornament ornament--top" role="img" aria-label="Small decorative flourish"></span>
      <p class="tagline">"All vegan, gluten free, organic,<br>fair trade chocolate <strong>that tastes amazing!</strong>"</p>
      <div class="rule"></div>
      <p class="origin">Locally Made<br>in Austin Texas</p>
      <p class="address">418 West Cobbler Ridge Rd #207 Austin Tx 78745</p>
      <div class="rule"></div>
      <p class="brand-name"><span class="brand-name__big">Willow</span><span class="brand-name__small">Bend</span><span class="brand-name__big">Sweets</span></p>
      <div class="rule"></div>
      <div class="contact">
        <p class="contact__item contact__web">willowbendsweetsatx.com</p>
        <p class="contact__item"><svg class="icon" viewBox="0 0 10 10"><path d="M2,0.5 L4,2.5 L3,4 Q4.5,6 6,7 L7.5,6 L9.5,8 L8,9.5 Q3,9 0.5,2 Z" fill="currentColor"/></svg>512.368.4175</p>
        <p class="contact__item"><span class="icon icon--square"></span>willowbendsweets</p>
      </div>
      <span class="ornament ornament--bottom" role="img" aria-label="Small decorative flourish"></span>
    </div>
  </article>

  <!-- Gradient sticker with white frame -->
  <article class="sticker sticker--framed">
    <svg class="sticker__shape" viewBox="0 0 150 560" aria-hidden="true">
      <defs>
        <linearGradient id="sunset-a" x1="0" y1="0" x2="0" y2="1">
          <stop offset="0" stop-color="#c8b9e6"/>
          <stop offset="0.3" stop-color="#f6c5c2"/>
          <stop offset="0.62" stop-color="#f8c8ae"/>
          <stop offset="0.7" stop-color="#f6e84e"/>
          <stop offset="1" stop-color="#fbc08a"/>
        </linearGradient>
      </defs>
      <rect width="150" height="560" fill="url(#sunset-a)"/>
      <path d="M8,42 L35,22 L55,36 L85,14 L110,34 L142,14 L142,546 L8,546 Z" fill="none" stroke="#ffffff" stroke-width="2"/>
    </svg>
    <div class="label">
      <span class="ornament ornament--top" role="img" aria-label="Small decorative flourish"></span>
      <p class="tagline">"All vegan, gluten free, organic,<br>fair trade chocolate <strong>that tastes amazing!</strong>"</p>
      <div class="rule"></div>
      <p class="origin">Locally Made<br>in Austin Texas</p>
      <p class="address">418 West Cobbler Ridge Rd #207 Austin Tx 78745</p>
      <div class="rule"></div>
      <p class="brand-name"><span class="brand-name__big">Willow</span><span class="brand-name__small">Bend</span><span class="brand-name__big">Sweets</span></p>
      <div class="rule"></div>
      <div class="contact">
        <p class="contact__item contact__web">willowbendsweetsatx.com</p>
        <p class="contact__item"><svg class="icon" viewBox="0 0 10 10"><path d="M2,0.5 L4,2.5 L3,4 Q4.5,6 6,7 L7.5,6 L9.5,8 L8,9.5 Q3,9 0.5,2 Z" fill="currentColor"/></svg>512.368.4175</p>
        <p class="contact__item"><span class="icon icon--square"></span>willowbendsweets</p>
      </div>
      <span class="ornament ornament--bottom" role="img" aria-label="Small decorative flourish"></span>
    </div>
  </article>

  <!-- Black panel on gradient -->
  <article class="sticker sticker--noir-inset">
    <svg class="sticker__shape" viewBox="0 0 150 560" aria-hidden="true">
      <defs>
        <linearGradient id="sunset-b" x1="0" y1="0" x2="0" y2="1">
          <stop offset="0" stop-color="#c8b9e6"/>
          <stop offset="0.3" stop-color="#f6c5c2"/>
          <stop offset="0.62" stop-color="#f8c8ae"/>
          <stop offset="0.7" stop-color="#f6e84e"/>
          <stop offset="1" stop-color="#fbc08a"/>
        </linearGradient>
      </defs>
      <rect width="150" height="560" fill="url(#sunset-b)"/>
      <path d="M0,42 L35,22 L55,36 L85,14 L110,34 L144,12 L144,540 L8,548 L8,42 Z" fill="#111111"/>
    </svg>
    <div class="label label--light">
      <span class="ornament ornament--top" role="img" aria-label="Small decorative flourish"></span>
      <p class="tagline">"All vegan, gluten free, organic,<br>fair trade chocolate <strong>that tastes amazing!</strong>"</p>
      <div class="rule"></div>
      <p class="origin">Locally Made<br>in Austin Texas</p>
      <p class="address">418 West Cobbler Ridge Rd #207 Austin Tx 78745</p>
      <div class="rule"></div>
      <p class="brand-name"><span class="brand-name__big">Willow</span><span class="brand-name__small">Bend</span><span class="brand-name__big">Sweets</span></p>
      <div class="rule"></div>
      <div class="contact">
        <p class="contact__item contact__web">willowbendsweetsatx.com</p>
        <p class="contact__item"><svg class="icon" viewBox="0 0 10 10"><path d="M2,0.5 L4,2.5 L3,4 Q4.5,6 6,7 L7.5,6 L9.5,8 L8,9.5 Q3,9 0.5,2 Z" fill="currentColor"/></svg>512.368.4175</p>
        <p class="contact__item"><span class="icon icon--square"></span>willowbendsweets</p>
      </div>
      <span class="ornament ornament--bottom" role="img" aria-label="Small decorative flourish"></span>
    </div>
  </article>

  <!-- White panel on gradient -->
  <article class="sticker sticker--white-inset">
    <svg class="sticker__shape" viewBox="0 0 150 560" aria-hidden="true">
      <defs>
        <linearGradient id="sunset-c" x1="0" y1="0" x2="0" y2="1">
          <stop offset="0" stop-color="#c8b9e6"/>
          <stop offset="0.3" stop-color="#f6c5c2"/>
          <stop offset="0.62" stop-color="#f8c8ae"/>
          <stop offset="0.7" stop-color="#f6e84e"/>
          <stop offset="1" stop-color="#fbc08a"/>
        </linearGradient>
      </defs>
      <rect width="150" height="560" fill="url(#sunset-c)"/>
      <path d="M8,44 L35,24 L55,38 L85,16 L110,36 L144,14 L144,540 L8,548 Z" fill="#ffffff"/>
    </svg>
    <div class="label">
      <span class="ornament ornament--top" role="img" aria-label="Small decorative flourish"></span>
      <p class="tagline">"All vegan, gluten free, organic,<br>fair trade chocolate <strong>that tastes amazing!</strong>"</p>
      <div class="rule"></div>
      <p class="origin">Locally Made<br>in Austin Texas</p>
      <p class="address">418 West Cobbler Ridge Rd #207 Austin Tx 78745</p>
      <div class="rule"></div>
      <p class="brand-name"><span class="brand-name__big">Willow</span><span class="brand-name__small">Bend</span><span class="brand-name__big">Sweets</span></p>
      <div class="rule"></div>
      <div class="contact">
        <p class="contact__item contact__web">willowbendsweetsatx.com</p>
        <p class="contact__item"><svg class="icon" viewBox="0 0 10 10"><path d="M2,0.5 L4,2.5 L3,4 Q4.5,6 6,7 L7.5,6 L9.5,8 L8,9.5 Q3,9 0.5,2 Z" fill="currentColor"/></svg>512.368.4175</p>
        <p class="contact__item"><span class="icon icon--square"></span>willowbendsweets</p>
      </div>
      <span class="ornament ornament--bottom" role="img" aria-label="Small decorative flourish"></span>
    </div>
  </article>

</main>
</body>
</html>
```